Wine Label Design for the red wine named “Amber Moth Ridge” or “A/M”

Create an elegant yet simple (less is more) label for a red, full-bodied wine from a family-owned Herzegovinian vineyard by the river with 9 names. You can use elements such as the Calopteryx virgo, possibly the river shape, and ensure a coherent storytelling of the unique vineyard’s locality and meticulous, hand-picked grape cultivation.
Let’s craft a label that is not just seen, but is experienced and remembered.

Target Market(s)

Wine lovers that appreciate high quality wines

Industry/Entity Type

Wine, Family owned small producer

Requirements
Must have
• Name A/M, front and back label. Premium feel, uniqueness. Simple but interesting.
Nice to have
• Please see the images below as an idea of various directions. I am also leaning to embossed image on the label
Should not have
• Should not be overcrowded with text, too many images and objects

```html
<!DOCTYPE html>
<html lang="en">
<head>
<meta charset="utf-8">
<title>Amber Moth Ridge — Wine Label</title>
<link rel="stylesheet" href="https://fonts.googleapis.com/css2?family=Italiana&family=Cormorant+Garamond:wght@400&display=swap">
<style>
  :root {
    --backdrop: #ececee;
    --paper: #fbfbfb;
    --ink: #1d1d1f;
    --mark-grey: #c9c9cc;
    --wine-deep: #5e1518;
    --wine: #7e2528;
    --wine-light: #9a3437;
    --cream: #f1e3e0;
  }
  * { margin: 0; padding: 0; box-sizing: border-box; }
  html, body {
    width: 1200px;
    height: 900px;
    overflow: hidden;
    background: var(--backdrop);
  }
  .canvas {
    position: relative;
    width: 1200px;
    height: 900px;
  }
  .label {
    position: absolute;
    left: 311px;
    top: 70px;
    width: 578px;
    height: 760px;
    background: var(--paper);
    border-radius: 8px;
    overflow: hidden;
  }
  .label__brand {
    position: absolute;
    left: 0;
    top: 0;
    width: 100%;
    height: 480px;
  }
  .brand-mark {
    position: absolute;
    top: 70px;
    width: 100%;
    text-align: center;
    font-family: "Italiana", serif;
    font-size: 170px;
    line-height: 1;
    color: var(--mark-grey);
  }
  .brand-name {
    position: absolute;
    top: 378px;
    width: 100%;
    text-align: center;
    font-family: "Italiana", serif;
    font-size: 46px;
    letter-spacing: 0.5px;
    color: var(--ink);
  }
  .label__band {
    position: absolute;
    left: 0;
    top: 480px;
    width: 100%;
    height: 280px;
  }
  .band-texture {
    position: absolute;
    inset: 0;
    background:
      radial-gradient(ellipse at 78% 55%, var(--wine-light) 0%, transparent 45%),
      radial-gradient(ellipse at 20% 30%, var(--wine-light) 0%, transparent 50%),
      linear-gradient(135deg, var(--wine-deep), var(--wine) 55%, var(--wine-deep));
  }
  .wine-style,
  .wine-region {
    position: absolute;
    width: 100%;
    text-align: center;
    font-family: "Cormorant Garamond", serif;
    color: var(--cream);
  }
  .wine-style {
    top: 184px;
    font-size: 36px;
  }
  .wine-region {
    top: 230px;
    font-size: 29px;
  }
</style>
</head>
<body>
  <main class="canvas">
    <section class="label">
      <header class="label__brand">
        <div class="brand-mark">A/M</div>
        <h1 class="brand-name">AMBER MOTH RIDGE</h1>
      </header>
      <div class="label__band">
        <div class="band-texture" role="img" aria-label="Marbled deep red wood-grain texture"></div>
        <p class="wine-style">Red / Full-Bodied</p>
        <p class="wine-region">Herzegovina</p>
      </div>
    </section>
  </main>
</body>
</html>
```